Harnwick Aerial Services, LLC - Business Card

I currently have a drone business that specializes in aerial photography, thermal image inspections, deer recovery, search and rescue, custom agricultural applications. i will attach my current business card as well as some logos to incorporate for a new up to date business card
Updates

Designs look the same

Sick

Target Market(s)

farmers, hunters

Contact Information for Business Card

name address phone number (as existing card i attached)

Requirements
Must have
• im good with existing business card, but would like an agricultural twist

```html
<!DOCTYPE html>
<html lang="en">
<head>
<meta charset="utf-8">
<title>Harnwick Aerial Services – Business Card</title>
<link href="https://fonts.googleapis.com/css2?family=Montserrat:wght@400;500;600;700&display=swap" rel="stylesheet">
<style>
  :root {
    --ink: #0b0b0b;
    --paper: #ffffff;
    --leaf: #3f9b3c;
    --leaf-light: #5cbf4f;
    --stage: #c9c9c9;
    --stage-dark: #a9a9a9;
  }
  * { margin: 0; padding: 0; box-sizing: border-box; }
  html, body {
    width: 1200px; height: 815px; overflow: hidden;
    background: radial-gradient(ellipse at 45% 30%, var(--stage) 0%, var(--stage-dark) 100%);
    font-family: "Montserrat", sans-serif;
  }
  .card {
    position: absolute; top: 253px;
    width: 540px; height: 309px;
    border-radius: 22px; overflow: hidden;
    box-shadow: 0 14px 30px rgba(0,0,0,.28);
    background: var(--ink);
  }
  .card--front { left: 45px; }
  .card--back { left: 615px; }
  .card__art { position: absolute; inset: 0; width: 100%; height: 100%; }

  /* Brand name */
  .brand {
    position: absolute; display: flex; align-items: center; gap: 10px;
    color: var(--leaf); font-weight: 700; letter-spacing: .5px;
  }
  .brand__dot {
    border-radius: 50%; border: 3px solid var(--leaf); flex: none;
  }
  .card--front .brand { left: 36px; top: 104px; font-size: 26px; }
  .card--front .brand__dot { width: 24px; height: 24px; }

  /* Front: person and contact */
  .person { position: absolute; right: 34px; top: 80px; text-align: right; }
  .person__name { color: var(--leaf-light); font-weight: 600; font-size: 21px; letter-spacing: 1px; }
  .person__role { color: var(--paper); font-size: 12px; letter-spacing: 1.5px; margin-top: 2px; }

  .contact { position: absolute; right: 34px; top: 150px; list-style: none; }
  .contact__item {
    display: flex; justify-content: flex-end; align-items: center; gap: 8px;
    color: var(--paper); font-size: 12.5px; line-height: 22px;
  }
  .contact__icon { width: 11px; height: 11px; fill: var(--leaf-light); flex: none; }

  .address {
    position: absolute; left: 38px; bottom: 28px;
    display: flex; align-items: flex-end; gap: 8px;
    color: var(--paper); font-size: 13px; line-height: 18px;
  }
  .address .contact__icon { margin-bottom: 3px; }

  /* Back */
  .card--back .brand {
    left: 0; right: 0; top: 82px; justify-content: center; font-size: 40px;
  }
  .card--back .brand__dot { width: 38px; height: 38px; }
  .services {
    position: absolute; left: 60px; right: 40px; top: 200px;
    list-style: none; display: flex; flex-wrap: wrap; column-gap: 16px; row-gap: 6px;
  }
  .services__item {
    color: var(--paper); font-size: 14px; display: flex; align-items: center; gap: 7px;
  }
  .services__item::before {
    content: ""; width: 7px; height: 7px; border-radius: 50%; background: var(--leaf-light);
  }
  .card__edge { position: absolute; left: 0; right: 0; bottom: 0; height: 4px; background: var(--leaf); }
</style>
</head>
<body>

<section class="card card--front" aria-label="Business card front">
  <svg class="card__art" viewBox="0 0 540 309" preserveAspectRatio="none" aria-hidden="true">
    <rect width="540" height="309" fill="var(--paper)"/>
    <path d="M0,196 C145,214 215,180 252,112 C282,56 305,14 350,0 L540,0 L540,309 L0,309 Z" fill="var(--leaf)"/>
    <path d="M0,212 C150,230 225,192 262,122 C292,66 315,28 355,14 C415,-4 500,4 540,14 L540,309 L0,309 Z" fill="var(--paper)"/>
    <path d="M0,222 C155,238 232,200 270,130 C300,75 322,38 362,24 C420,6 500,12 540,22 L540,309 L0,309 Z" fill="var(--ink)"/>
  </svg>

  <div class="brand"><span class="brand__dot"></span>Harnwick</div>

  <div class="person">
    <div class="person__name">WARREN HOLT</div>
    <div class="person__role">OWNER</div>
  </div>

  <ul class="contact">
    <li class="contact__item">555-014-2286
      <svg class="contact__icon" viewBox="0 0 24 24"><path d="M6.6 10.8a15.1 15.1 0 0 0 6.6 6.6l2.2-2.2c.3-.3.7-.4 1-.2 1.1.4 2.3.6 3.6.6.6 0 1 .4 1 1V20c0 .6-.4 1-1 1A17 17 0 0 1 3 4c0-.6.4-1 1-1h3.5c.6 0 1 .4 1 1 0 1.3.2 2.5.6 3.6.1.3 0 .7-.2 1z"/></svg>
    </li>
    <li class="contact__item">hello@harnwickaerial.com
      <svg class="contact__icon" viewBox="0 0 24 24"><path d="M2 5h20v14H2z M2 5l10 8 10-8" stroke="var(--ink)" stroke-width="1.5"/></svg>
    </li>
    <li class="contact__item">www.harnwickaerial.com
      <svg class="contact__icon" viewBox="0 0 24 24"><circle cx="12" cy="12" r="10"/><path d="M2 12h20M12 2c3 3 3 17 0 20M12 2c-3 3-3 17 0 20" stroke="var(--ink)" stroke-width="1.5" fill="none"/></svg>
    </li>
  </ul>

  <div class="address">
    <svg class="contact__icon" viewBox="0 0 24 24"><path d="M12 2a7 7 0 0 0-7 7c0 5 7 13 7 13s7-8 7-13a7 7 0 0 0-7-7zm0 9.5A2.5 2.5 0 1 1 12 6.5a2.5 2.5 0 0 1 0 5z"/></svg>
    <div>214 W. Orchard St.<br>Fairhaven, OH 45390</div>
  </div>
  <div class="card__edge"></div>
</section>

<section class="card card--back" aria-label="Business card back">
  <div class="brand"><span class="brand__dot"></span>Harnwick</div>
  <ul class="services">
    <li class="services__item">Thermal Image Inspections</li>
    <li class="services__item">Deer Recovery</li>
    <li class="services__item">Search &amp; Rescue</li>
    <li class="services__item">Real Estate Photography</li>
  </ul>
  <div class="card__edge"></div>
</section>

</body>
</html>
```